Real Estate Design Website

I would like to have a design for "real estate agent" website. It needs to be in a "Responsive" framework.

The design need to be suitable for different viewer from all around the world. It needs to be modern. It'd be great if there is a design for mobile and vexo/tablet (it's all under responsive framework). It needs to be easy to navigate and look modern

Target Market(s)

End user/Real estate buyers from different part of the world

Industry/Entity Type

Real Estate

Requirements
Must have
• It's for real estate agent website which is used to represent their brand/image but at the same time it also for their client which is real estate buyers
Should not have
• Should not be boring design/out of date

```html
<!DOCTYPE html>
<html lang="en">
<head>
<meta charset="utf-8">
<title>Halden – Cyprus Property</title>
<link href="https://fonts.googleapis.com/css2?family=Open+Sans:wght@400;600;700&family=Arimo:wght@400;700&display=swap" rel="stylesheet">
<style>
:root{
  --blue:#1b8fd8;
  --blue-dark:#0f6fb3;
  --ink:#333;
  --muted:#666;
  --paper:#eeeeec;
  --footer:#e2e2e0;
  --price:#d4531b;
  --line:#cfcfcf;
}
*{box-sizing:border-box;margin:0;padding:0}
html,body{width:734px;height:1200px;overflow:hidden}
body{background:var(--paper);font-family:Arimo,Arial,sans-serif;color:var(--ink);position:relative;font-size:8px}
.abs{position:absolute}
.brand{left:96px;top:22px;font:700 20px/24px "Open Sans",sans-serif;color:var(--blue);letter-spacing:1px}
.tagline{left:74px;top:50px;font-size:8px;line-height:10px;color:#555}
.account{right:76px;top:20px;font-size:8px;color:var(--blue)}
.account span{color:#999;margin:0 5px}
.btn{background:var(--blue);color:#fff;font-size:7px;text-align:center;border-radius:1px}
.submit{left:574px;top:44px;width:84px;height:18px;line-height:18px}
.nav{left:0;top:72px;width:734px;height:26px;background:var(--blue);border-top:2px solid #5fb6ea}
.nav ul{list-style:none;display:flex;margin-left:70px}
.nav li{color:#fff;font-size:8px;line-height:24px;padding:0 8px;text-transform:uppercase}
.nav li.active{background:#5db3e8}
.hero{left:0;top:98px;width:734px;height:300px;background:linear-gradient(180deg,#8fb070 0%,#5f7f46 40%,#8a8a7a 70%,#4f6e3a 100%)}
.hero-shadow{left:160px;top:398px;width:414px;height:18px;background:radial-gradient(ellipse at top,rgba(0,0,0,.35),transparent 70%)}
.search{left:463px;top:122px;width:173px;height:270px;background:rgba(240,240,240,.82)}
.search h3{position:absolute;left:18px;top:12px;font:400 11px "Open Sans",sans-serif;color:var(--blue-dark)}
.search .tabs{position:absolute;left:18px;top:42px;width:137px;display:flex;justify-content:space-between;font-size:8px;color:var(--blue)}
.sel{position:absolute;height:18px;background:#fff;font-size:7px;color:#444;line-height:18px;padding-left:4px}
.sel::after{content:"";position:absolute;right:0;top:0;width:16px;height:18px;background:var(--blue)}
.sel::before{content:"";position:absolute;right:5px;top:7px;border:3px solid transparent;border-top:4px solid #fff;z-index:1}
.search .go{position:absolute;left:91px;top:204px;width:64px;height:18px;line-height:18px}
.search .adv{position:absolute;right:18px;top:232px;font-size:8px;color:var(--blue)}
.feature{width:150px;text-align:center;top:438px}
.feature .icon{width:60px;height:60px;border-radius:50%;margin:0 auto;background:#e6e6e4;display:flex;align-items:center;justify-content:center}
.feature .icon.on{background:#3a3a3a;border:3px solid var(--blue)}
.feature h2{font:400 14px "Open Sans",sans-serif;margin-top:12px}
.feature p{font-size:7px;color:#555;margin-top:4px;line-height:9px}
.feature .more{display:inline-block;margin-top:14px;width:51px;height:15px;line-height:15px;background:var(--blue-dark);color:#fff;font-size:6px}
.sec-title{font:600 10.5px "Open Sans",sans-serif;color:#333;display:flex;align-items:center;text-transform:uppercase}
.sec-title::after{content:"";flex:1;height:5px;margin-left:6px;background:repeating-linear-gradient(135deg,#bbb 0 1px,transparent 1px 3px)}
.col{top:631px}
.col p{font-size:7.5px;line-height:10px;color:#333;margin-top:14px}
.col .sig{font-style:italic;margin-top:8px}
.news{left:475px;top:660px;width:185px;height:58px;background:#d9d9d7}
.news p{position:absolute;left:10px;top:10px;font-size:7px;color:#555}
.news .email{position:absolute;left:10px;top:25px;width:120px;height:18px;background:#fff;font-size:7px;line-height:18px;padding-left:5px}
.news .subs{position:absolute;left:130px;top:25px;width:45px;height:18px;line-height:18px}
.card{top:784px;width:181px}
.card .photo{height:104px;border:3px solid #fff;box-shadow:0 0 1px #aaa}
.card h4{font:700 9.5px "Open Sans",sans-serif;color:#555;margin-top:7px;display:flex;justify-content:space-between}
.card h4 em{font:italic 400 8px Arimo,sans-serif;color:var(--blue)}
.card .specs{border-top:1px solid var(--line);border-bottom:1px solid var(--line);margin-top:4px;padding:4px 0;font-size:7px;color:#555;display:flex;gap:14px}
.card .foot{display:flex;justify-content:space-between;align-items:center;margin-top:8px}
.card .price{font:700 12px "Open Sans",sans-serif;color:var(--price)}
.card .view{width:68px;height:18px;line-height:18px}
.ribbon{position:absolute;left:0;top:0;width:40px;height:40px;background:linear-gradient(135deg,var(--blue) 50%,transparent 50%)}
.footer{left:0;top:994px;width:734px;height:172px;background:var(--footer)}
.fcol{top:1016px}
.fcol p{font-size:7.5px;line-height:10px;margin-top:14px}
.post{display:flex;gap:8px;margin-top:12px;font-size:7.5px;line-height:10px}
.post .face{width:36px;height:36px;border-radius:50%;border:2px solid #fff;flex:none}
.post small{display:block;font-style:italic;color:#777;font-size:6.5px}
.contact li{list-style:none;display:flex;gap:10px;font-size:7.5px;line-height:16px}
.contact li i{width:10px;flex:none}
.bottom{left:0;top:1166px;width:734px;height:34px;background:var(--blue);color:#fff}
.bottom p{position:absolute;left:74px;top:13px;font-size:7px}
.social{position:absolute;left:563px;top:8px;display:flex;gap:5px}
.social span{width:20px;height:20px;background:#0d5f96;border-radius:2px}
.totop{position:absolute;right:0;top:0;width:36px;height:34px;background:#0d6ba8}
</style>
</head>
<body>
<div class="abs brand">Halden</div>
<div class="abs tagline">Cyprus property For Sale and For Rent</div>
<div class="abs account">Welcome , Guest<span>|</span>Sign In<span>|</span>Sign Up</div>
<div class="abs btn submit">Submit Property &gt;&gt;</div>

<nav class="abs nav"><ul>
<li class="active">Home</li><li>About us</li><li>Featured</li><li>Home buyers</li><li>Home sellers</li><li>Team</li><li>Contact us</li>
</ul></nav>

<div class="abs hero" role="img" aria-label="Photo of a two-storey suburban house with lawn and trees"></div>
<div class="abs hero-shadow"></div>
<form class="abs search">
<h3>QUICK SEARCH</h3>
<div class="tabs"><span>For sale</span><span>For Rent</span></div>
<div class="sel" style="left:18px;top:64px;width:137px">Location</div>
<div class="sel" style="left:18px;top:90px;width:137px">Property type</div>
<div class="sel" style="left:18px;top:116px;width:137px">Square Feet</div>
<div class="sel" style="left:18px;top:148px;width:65px">Beds</div>
<div class="sel" style="left:90px;top:148px;width:65px">Baths</div>
<div class="sel" style="left:18px;top:174px;width:65px">Min price</div>
<div class="sel" style="left:90px;top:174px;width:65px">Max price</div>
<div class="btn go">Search</div>
<div class="adv">Advanced Search</div>
</form>

<section class="abs feature" style="left:97px">
<div class="icon on"><svg width="22" height="28" viewBox="0 0 22 28"><path d="M11 0a10 10 0 0 0-10 10c0 8 10 18 10 18s10-10 10-18A10 10 0 0 0 11 0z" fill="#fff"/><circle cx="11" cy="10" r="5" fill="#3a3a3a"/><path d="M11 7v6M8 10h6" stroke="#fff" stroke-width="1.5"/></svg></div>
<h2>Listing</h2>
<p>Lorem ipsum dolor sit amet, consectetur adipisicing elit, sed do eiusmod tempor incididunt ut labore et dolore magna aliqua</p>
<span class="more">Read more &gt;</span>
</section>
<section class="abs feature" style="left:291px">
<div class="icon"><svg width="30" height="30" viewBox="0 0 30 30"><circle cx="15" cy="15" r="10" fill="none" stroke="#555" stroke-width="3"/><path d="M15 1v6M15 23v6M1 15h6M23 15h6" stroke="#555" stroke-width="3"/><path d="M19 11l-6 2-2 6 6-2z" fill="#555"/></svg></div>
<h2>Advertise</h2>
<p>Lorem ipsum dolor sit amet, consectetur adipisicing elit, sed do eiusmod tempor incididunt ut labore et dolore magna aliqua</p>
<span class="more">Read more &gt;</span>
</section>
<section class="abs feature" style="left:487px">
<div class="icon"><svg width="32" height="14" viewBox="0 0 32 14"><circle cx="7" cy="7" r="6" fill="#555"/><circle cx="7" cy="7" r="2" fill="#e6e6e4"/><path d="M12 5h19v4h-3v4h-3V9h-3v3h-3V9h-7z" fill="#555"/></svg></div>
<h2>Guidance</h2>
<p>Lorem ipsum dolor sit amet, consectetur adipisicing elit, sed do eiusmod tempor incididunt ut labore et dolore magna aliqua</p>
<span class="more">Read more &gt;</span>
</section>

<section class="abs col" style="left:74px;width:185px">
<h3 class="sec-title">Why chose us?</h3>
<p>Lorem ipsum dolor sit amet, consectetur adipisicing elit, sed do eiusmod tempor incididunt ut labore et dolore magna aliqua. Ut enim ad minim veniam, quis nostrud exercitation ullamco laboris nisi ut aliquip ex ea commodo consequat. Duis aute irure dolor in reprehenderit in voluptate velit esse cillum</p>
</section>
<section class="abs col" style="left:274px;width:185px">
<h3 class="sec-title">Happy clints</h3>
<p>Sed ut perspiciatis unde omnis iste natus error sit voluptatem accusantium doloremque laudantium, totam rem aperiam, eaque ipsa quae ab illo inventore veritatis et quasi architecto beatae vitae dicta sunt explicabo.</p>
<p class="sig">John W Doe-Los Angeles</p>
</section>
<section class="abs col" style="left:475px;width:185px">
<h3 class="sec-title">Newsletter!</h3>
</section>
<div class="abs news">
<p>Stay updated with all latest news.</p>
<div class="email">Email</div>
<div class="btn subs">Subscribe</div>
</div>

<h3 class="abs sec-title" style="left:74px;top:757px;width:586px">Last hour properties</h3>

<article class="abs card" style="left:74px">
<div class="photo" role="img" aria-label="Photo of a large grey family house with garage" style="background:linear-gradient(180deg,#a9c4e6 0%,#c9cfd6 45%,#8d8f8c 75%,#6d8a4e 100%)"></div>
<h4>8302 Vercelli Court <em>For Sale</em></h4>
<div class="specs"><span>▭ 2 Bedrooms</span><span>⌂ 2198 sqft</span><span>◌ 4 baths</span></div>
<div class="foot"><span class="price">$192,000</span><span class="btn view">View details</span></div>
</article>
<article class="abs card" style="left:275px">
<div class="photo" role="img" aria-label="Photo of a brick house with a lawn at dusk" style="background:linear-gradient(180deg,#4a5560 0%,#5d5347 50%,#3f4a34 100%)"></div>
<h4>8302 Vercelli Court <em>For Sale</em></h4>
<div class="specs"><span>▭ 2 Bedrooms</span><span>⌂ 2198 sqft</span><span>◌ 4 baths</span></div>
<div class="foot"><span class="price">$192,000</span><span class="btn view">View details</span></div>
</article>
<article class="abs card" style="left:475px">
<div class="photo" role="img" aria-label="Photo of a beige stone house with garage" style="background:linear-gradient(180deg,#bcd2ea 0%,#c7b49a 45%,#9a8a74 75%,#6c7d4e 100%);position:relative"><span class="ribbon"></span></div>
<h4>8302 Vercelli Court <em>For Sale</em></h4>
<div class="specs"><span>▭ 2 Bedrooms</span><span>⌂ 2198 sqft</span><span>◌ 4 baths</span></div>
<div class="foot"><span class="price">$192,000</span><span class="btn view">View details</span></div>
</article>

<footer class="abs footer"></footer>
<section class="abs fcol" style="left:74px;width:185px">
<h3 class="sec-title">About us</h3>
<p>Lorem ipsum dolor sit amet elit, consectetur adipiscing. Vestibulum luctus ipsum id quam euismod a malesuada sapien euismod. Vesti bulum ultricies elementum interdum.</p>
<p>Read more &gt;&gt;</p>
</section>
<section class="abs fcol" style="left:274px;width:185px">
<h3 class="sec-title">From the blog</h3>
<div class="post"><span class="face" role="img" aria-label="Author portrait" style="background:#9aa3ad"></span><div>Sed ut perspiciatis unde omnis iste natus error sit voluptatem<small>22January 2013</small></div></div>
<div style="border-top:1px solid #bbb;margin-top:6px"></div>
<div class="post" style="margin-top:6px"><span class="face" role="img" aria-label="Author portrait" style="background:#c2b3a6"></span><div>Sed ut perspiciatis unde omnis iste natus error sit voluptatem<small>22January 2013</small></div></div>
</section>
<section class="abs fcol contact" style="left:475px;width:185px">
<h3 class="sec-title">Contact us</h3>
<ul style="margin-top:10px">
<li><i><svg width="8" height="10" viewBox="0 0 8 10"><path d="M4 0a4 4 0 0 0-4 4c0 3 4 6 4 6s4-3 4-6a4 4 0 0 0-4-4z" fill="#555"/><circle cx="4" cy="4" r="1.4" fill="#e2e2e0"/></svg></i>No 18 Linden Row 42/7 Westbrook</li>
<li><i></i>City , WB Harbor Coast</li>
<li><i><svg width="9" height="7" viewBox="0 0 9 7"><rect width="9" height="7" fill="#555"/><path d="M0 0l4.5 4L9 0" stroke="#e2e2e0" fill="none"/></svg></i>abcde@postmail.net</li>
<li><i></i>abcdef@postmail.net</li>
<li><i><svg width="10" height="8" viewBox="0 0 10 8"><path d="M0 2q5-3 10 0v2H7V3H3v1H0z" fill="#555"/><rect x="2" y="4" width="6" height="4" fill="#555"/></svg></i>(+00) 05550100-234</li>
<li><i></i>(+00) 05550100-234</li>
</ul>
</section>

<div class="abs bottom">
<p>Copyright © 2013 Company Name. All rights reserved.</p>
<div class="social"><span></span><span></span><span></span><span></span></div>
<div class="totop"><svg width="36" height="34" viewBox="0 0 36 34"><path d="M10 21l8-8 8 8" stroke="#fff" stroke-width="2" fill="none"/></svg></div>
</div>
</body>
</html>
```